New, modern business card for growing audiology practice

We need a new business card for our audiology practice. Our logo and website have recently changed (more modern) and we want our business cards to reflect this change.
We conduct hearing tests, perform earwax removals, and fit & dispense hearing aids to our patients. We are a family owned practice in which the owner is the one who works directly with the patient. I have attached logos in various formats to use, as well as two ideas I found on this website; as well as a scanned copy of our current logo. Good luck!

Industry/Entity Type

Business

Contact Information for Business Card

Company name: Maplow Hearing Center
Provider name: Peter Mulvoy, Au.D. F/ISN
Phone number: (555) 318-6042
Address: 87 W. Linden Ave. Brookden Falls, OH 40917
email: maplowhearing@postvale.net
website: maplowhearing.com

Colors
000000
aaaaaa
dbdbdb
cacaca
9bcb3c
afd23c
cadf82
b1b1b1

Requirements
Must have
• My card must include information in the "details" section. In the attached images, I found a few that I liked and I would like to model after - "brisk tumblin'" and "Sound Wellness Center".
• Must be horizontal.
• Must include logos provided. I uploaded them in various file formats and various ways.
• Must match logo font, if possible, if not, please get as close as you can.
Nice to have
• I really like the idea of having a color on one side with just the logo and company name and the contact information and provider name on the other side. I also really like the idea of having the main color dominating on the logo/company side with accent of that same color on the contact side of the card.
Should not have
• Must not be vertical.

```html
<!DOCTYPE html>
<html lang="en">
<head>
<meta charset="utf-8">
<title>Maplow Hearing Center – Business Card</title>
<link rel="stylesheet" href="https://fonts.googleapis.com/css2?family=Open+Sans:wght@300;400;600;700&display=swap">
<style>
  :root {
    --green: #8cc03a;
    --green-light: #afd23c;
    --green-pale: #cadf82;
    --ink: #111111;
    --card-black: #161616;
    --white: #ffffff;
    --backdrop: #dbdbdb;
  }
  * { box-sizing: border-box; margin: 0; padding: 0; }
  html, body {
    width: 1200px; height: 900px; overflow: hidden;
    background: var(--backdrop);
    font-family: "Open Sans", sans-serif;
  }
  .canvas { position: relative; width: 1200px; height: 900px; }
  .card {
    position: absolute; left: 300px;
    width: 600px; height: 343px;
    border-radius: 6px; overflow: hidden;
    box-shadow: 0 10px 30px rgba(0,0,0,0.25);
  }
  .card-front {
    top: 70px;
    background: var(--green);
    display: flex; align-items: center; justify-content: center;
  }
  .card-back { top: 487px; background: var(--card-black); }
  .brand {
    display: flex; align-items: center; gap: 12px;
    color: var(--ink);
    font-weight: 400;
    letter-spacing: 0.04em;
    text-transform: uppercase;
    white-space: nowrap;
  }
  .brand-dot {
    width: 26px; height: 26px; border-radius: 50%;
    background: var(--white);
    flex: none;
  }
  .card-front .brand { font-size: 30px; }
  .back-panel { position: absolute; inset: 0; width: 600px; height: 343px; }
  .card-back .brand {
    position: absolute; left: 34px; top: 44px;
    font-size: 18px;
  }
  .card-back .brand-dot { width: 20px; height: 20px; }
  .provider {
    position: absolute; right: 36px; top: 128px;
    text-align: right;
  }
  .provider-name {
    color: var(--white); font-weight: 400;
    font-size: 22px; letter-spacing: 0.06em; text-transform: uppercase;
  }
  .provider-title {
    color: var(--green); font-size: 14px; font-weight: 600;
    letter-spacing: 0.04em; margin-top: 2px;
  }
  .contact {
    position: absolute; right: 36px; top: 200px;
    list-style: none; text-align: right;
  }
  .contact li {
    display: flex; align-items: center; justify-content: flex-end; gap: 8px;
    color: var(--white); font-size: 14px; line-height: 21px;
  }
  .contact svg { width: 14px; height: 14px; flex: none; }
  .address {
    position: absolute; right: 36px; top: 270px;
    text-align: right; font-style: normal;
    color: var(--white); font-size: 14px; line-height: 19px; font-weight: 600;
  }
  .address-name { color: var(--green); font-weight: 700; }
</style>
</head>
<body>
<main class="canvas">

  <section class="card card-front" aria-label="Business card front">
    <div class="brand"><span class="brand-dot"></span>Maplow Hearing Center</div>
  </section>

  <section class="card card-back" aria-label="Business card back">
    <svg class="back-panel" viewBox="0 0 600 343" aria-hidden="true">
      <path d="M0 0 H372 C420 0 420 60 392 100 C360 148 310 180 262 220 C220 258 200 300 192 343 H0 Z" fill="var(--green)"/>
      <path d="M372 0 C420 0 420 60 392 100 C360 148 310 180 262 220 C220 258 200 300 192 343" fill="none" stroke="var(--green-pale)" stroke-width="6"/>
    </svg>

    <div class="brand"><span class="brand-dot"></span>Maplow Hearing Center</div>

    <div class="provider">
      <p class="provider-name">Peter Mulvoy</p>
      <p class="provider-title">Au.D. F/ISN</p>
    </div>

    <ul class="contact">
      <li>(555) 318-6042
        <svg viewBox="0 0 14 14"><circle cx="7" cy="7" r="7" fill="var(--green)"/><path d="M4 3.5 l2 0 0.6 2 -1 0.8 a5 5 0 0 0 2.1 2.1 l0.8 -1 2 0.6 0 2 a1 1 0 0 1 -1 0.5 A6.5 6.5 0 0 1 3.5 4.5 1 1 0 0 1 4 3.5z" fill="var(--card-black)"/></svg>
      </li>
      <li>maplowhearing@postvale.net
        <svg viewBox="0 0 14 14"><circle cx="7" cy="7" r="7" fill="var(--green)"/><rect x="3.5" y="4.5" width="7" height="5" fill="var(--card-black)"/><path d="M3.5 4.5 L7 7.5 L10.5 4.5" fill="none" stroke="var(--green)" stroke-width="0.8"/></svg>
      </li>
      <li>www.maplowhearing.com
        <svg viewBox="0 0 14 14"><circle cx="7" cy="7" r="7" fill="var(--green)"/><circle cx="7" cy="7" r="3.6" fill="none" stroke="var(--card-black)" stroke-width="1"/><path d="M3.4 7 H10.6 M7 3.4 V10.6" stroke="var(--card-black)" stroke-width="0.8"/></svg>
      </li>
    </ul>

    <address class="address">
      <span class="address-name">Maplow Hearing Center</span><br>
      87 W. Linden Ave. Brookden Falls<br>
      OH 40917
    </address>
  </section>

</main>
</body>
</html>
```